High end business card design for custom homebuilding company

Looking for a high end business card design that is unique and elegant. Can use embossing, foil printing, laser die cutting, or any high end printing technique or high end paper. Will upload current design so you can see the logo and what we are using currently, but we want something more unique and elegant. I included our logo to help with design.

Target Market(s)

High end custom home buyers of $1.5 million plus homes. Also real estate developers of high end communities.

Industry/Entity Type

Business

Contact Information for Business Card

Double sided. We want something very elegant and expensive looking. We are looking to incorporate a combination of perhaps linen paper or a high end paper, with foil stamping or embossing/debossing to make the card look unique, but still elegant. We tend to use blacks and golds, but are open to any ideas. Looking for creative and unique design.

Colors

Designer to choose colors to be used in the design.

Requirements
Must have
• High end, elegant look. Can use foil, embossing, or high end papers like linen. We want to make the card unique and interesting, but elegant and expensive looking.
Nice to have
• I am including just some cards I saw that looked interesting for one reason or another. I like a clean elegant design and like both the clean white style, and the blacks. So not sure if we want a black design or white. Would like to see both.

```html
<!DOCTYPE html>
<html lang="en">
<head>
<meta charset="utf-8">
<title>Larkfield Custom Homes – Business Card</title>
<link rel="stylesheet" href="https://fonts.googleapis.com/css2?family=Roboto:wght@400;500;700&display=swap">
<style>
  :root {
    --bg: #5c5f66;
    --gold-dark: #8a7a2c;
    --gold-mid: #b8a644;
    --gold-light: #e4dc86;
    --black-band: #1c1c1c;
    --black-band-light: #333333;
    --ink: #1a1a1a;
    --paper: #ffffff;
    --paper-tint: #f4f2ea;
    --icon-gold: #a8953a;
  }
  * { box-sizing: border-box; margin: 0; padding: 0; }
  html, body { width: 1200px; height: 1200px; overflow: hidden; }
  body {
    background: var(--bg);
    font-family: "Roboto", Arial, sans-serif;
    color: var(--ink);
    position: relative;
  }
  .card {
    position: absolute;
    left: 180px;
    width: 840px;
    height: 480px;
    background: linear-gradient(120deg, var(--gold-dark) 0%, var(--gold-mid) 35%, var(--gold-light) 55%, var(--gold-mid) 75%, var(--gold-dark) 100%);
    box-shadow: 0 10px 30px rgba(0,0,0,0.35);
  }
  .card--front { top: 80px; }
  .card--back { top: 640px; }

  /* Front side */
  .quilt-band {
    position: absolute;
    left: 60px;
    right: 60px;
    height: 112px;
    background: linear-gradient(180deg, var(--black-band-light) 0%, var(--black-band) 60%, var(--black-band-light) 100%);
  }
  .quilt-band--top { top: 52px; }
  .quilt-band--bottom { bottom: 52px; }
  .front-brand {
    position: absolute;
    top: 164px;
    height: 152px;
    left: 0;
    right: 0;
    display: flex;
    flex-direction: column;
    justify-content: center;
    align-items: center;
  }
  .brand-name {
    font-weight: 500;
    text-transform: uppercase;
    color: var(--ink);
    letter-spacing: 0.06em;
    white-space: nowrap;
  }
  .front-brand .brand-name { font-size: 44px; line-height: 1.1; }
  .front-website {
    margin-top: 12px;
    font-size: 22px;
    color: var(--ink);
  }

  /* Back side */
  .back-panel {
    position: absolute;
    inset: 56px 64px;
    background: var(--paper);
    overflow: hidden;
  }
  .back-pattern {
    position: absolute;
    inset: 0;
    background: radial-gradient(ellipse at 30% 40%, var(--paper-tint) 0%, var(--paper) 70%);
  }
  .back-content { position: relative; height: 100%; }
  .back-brand {
    position: absolute;
    top: 62px;
    left: 44px;
  }
  .back-brand .brand-name { font-size: 40px; }
  .holder-name {
    position: absolute;
    top: 160px;
    left: 0; right: 0;
    text-align: center;
    font-size: 22px;
  }
  .holder-name strong { font-weight: 700; }
  .contact-row {
    position: absolute;
    top: 232px;
    left: 30px;
    right: 30px;
    display: flex;
    justify-content: space-between;
    align-items: center;
    font-size: 18px;
  }
  .contact-item { display: flex; align-items: center; gap: 6px; white-space: nowrap; }
  .contact-item svg { width: 22px; height: 22px; flex: none; }
  .back-website {
    position: absolute;
    top: 290px;
    left: 0; right: 0;
    text-align: center;
    font-size: 17px;
  }
</style>
</head>
<body>

<section class="card card--front" aria-label="Card front">
  <div class="quilt-band quilt-band--top" role="img" aria-label="Black quilted diamond pattern band with gold studs"></div>
  <div class="front-brand">
    <div class="brand-name">Larkfield Custom Homes</div>
    <div class="front-website">www.larkfieldhomes.com.au</div>
  </div>
  <div class="quilt-band quilt-band--bottom" role="img" aria-label="Black quilted diamond pattern band with gold studs"></div>
</section>

<section class="card card--back" aria-label="Card back">
  <div class="back-panel">
    <div class="back-pattern" role="img" aria-label="Faint repeating brand pattern on white paper"></div>
    <div class="back-content">
      <div class="back-brand"><span class="brand-name">Larkfield Custom Homes</span></div>
      <p class="holder-name"><strong>DUMMY</strong> Name</p>
      <div class="contact-row">
        <span class="contact-item">
          <svg viewBox="0 0 24 24" aria-hidden="true"><rect x="7" y="2" width="10" height="20" rx="2" fill="none" stroke="var(--icon-gold)" stroke-width="1.6"/><circle cx="12" cy="18.5" r="1" fill="var(--icon-gold)"/></svg>
          012 . 555 . 0142
        </span>
        <span class="contact-item">
          <svg viewBox="0 0 24 24" aria-hidden="true"><circle cx="12" cy="12" r="9" fill="none" stroke="var(--icon-gold)" stroke-width="1.6"/><rect x="7" y="8.5" width="10" height="7" fill="none" stroke="var(--icon-gold)" stroke-width="1.3"/><path d="M7 8.5 L12 12.5 L17 8.5" fill="none" stroke="var(--icon-gold)" stroke-width="1.3"/></svg>
          info@larkfieldhomes.com
        </span>
        <span class="contact-item">
          <svg viewBox="0 0 24 24" aria-hidden="true"><circle cx="12" cy="12" r="9" fill="none" stroke="var(--icon-gold)" stroke-width="1.6"/><path d="M12 17 C9 13.5 8.5 12 8.5 10.5 A3.5 3.5 0 0 1 15.5 10.5 C15.5 12 15 13.5 12 17Z" fill="none" stroke="var(--icon-gold)" stroke-width="1.3"/><circle cx="12" cy="10.5" r="1.2" fill="var(--icon-gold)"/></svg>
          18 Elm Rd, Ashby
        </span>
      </div>
      <p class="back-website">www.larkfieldhomes.com.au</p>
    </div>
  </div>
</section>

</body>
</html>
```